Web design for facial expression recognition service

We offer a service which allows customers to film large panels of participants looking at some video/screen (e.g. an advertisement) and to analyze the facial expressions shown by the participants. We are looking for the design of a new website which will make it easy for our customers to setup and view the results of these experiments online.
Competitor's websites that may serve as a reference are:
http://www.moravelt.example/pindor/#pane_overview
http://www.quintabrook.example/homepage.aspx
https://www.tavorlin.example/
The website will (for as far as the design is concerned) consist of three parts:
- A public home page (and perhaps some contact/news/about page), designed to catch the attention/interest potential customers.
- A (protected) project result page, showing the results in an interactive page with charts and numerical data.
- Pages (also protected) with fields and tables (setting up the project details).
The winner of this design project should provide us with at least one design for each of the above in order to get a complete 'theme' going which our developers can use. However, you are welcome to initially only provide the design for the project result page and/or home page.
We are looking for a modern, fresh, yet professional look (my client is a more established party in the field).
The final delivery should consist of layered Photoshop or Illustrator files.
Thank you in advance for participating!
Dear designers,
Reason: Extending the deadline by a few days to give designers a chance to submit designs for the other pages and process further feedback.
Target Market(s)
marketing research agencies (B2B service)
Industry/Entity Type
Delivery
Requirements
Must have
- Home page:
- Basic advertisement of the service; some quick explanation of how it works
- A way to login for existing users
- A link/button/banner inviting people to sign up
- Navigation controls to 2-3 other pages
- Social media links (Chatterbay, WorkNest group)
- Company logo (sorry, can't provide it as my client wishes to remain anonymous for now, but it's rounded and has blue as it's main color).
- Copyright / creator details
Project result page:
(see attachment 1 for a functional mockup - the design may follow this layout closely, or be completely different)
- Title
- A video player and basic numerical data
- Different views of the analysis results can dynamically be added/removed/collapsed/expanded; each one of these views will show some kind of chart, filters (combos), numerical data and a download button/link.
- A way to sign out, go to the main project page and go to the main page
- Logo
- Copyright
The form pages:
(see attachment 2 for a functional mockup of one of the pages; feel free to change some elements to better show the overall style)
- Title
- Text fields, combos, calendar pickers, tables, navigation links
- Logo
- Copyright
Nice to have
- Any creative text elements or product logo/symbol are a bonus. However, the basic "Lorem Ipsum" would do too.

```html
<!DOCTYPE html>
<html lang="en">
<head>
<meta charset="utf-8">
<title>Veldhaven – Facial Expression Analysis</title>
<link href="https://fonts.googleapis.com/css2?family=PT+Sans:ital,wght@0,400;0,700;1,400;1,700&display=swap" rel="stylesheet">
<style>
:root{
  --blue-deep:#0a5fa8;
  --blue-mid:#0f78c8;
  --blue-light:#5ab4e8;
  --cyan:#3fd0f5;
  --bar-dark:#262626;
  --bar-mid:#444;
  --row-bg:#e9e9e9;
  --line:#d4d4d4;
  --text:#444;
  --text-soft:#888;
  --btn-grey:#707070;
  --green:#8ccc1a;
  --green-dark:#2f5a05;
  --footer:#0b65b0;
}
*{box-sizing:border-box;margin:0;padding:0}
html,body{width:1200px;height:1090px;overflow:hidden;background:#fff}
body{font-family:"PT Sans",sans-serif;color:var(--text);position:relative}
.abs{position:absolute}
.topbar{left:0;top:0;width:1200px;height:44px;background:linear-gradient(#4a4a4a,var(--bar-dark))}
.toplink{top:15px;font-size:10px;color:#bbb}
.topsep{top:14px;font-size:10px;color:#999}
.login{left:943px;top:8px;width:75px;height:27px;border-radius:4px;background:linear-gradient(#2a2a2a,#1a1a1a);border:1px solid #555;color:#ddd;font-size:12px;padding:5px 0 0 14px}
.login .chev{position:absolute;right:10px;top:7px;width:12px;height:12px;border-radius:50%;background:#eee}
.hero{left:0;top:44px;width:1200px;height:450px;background:linear-gradient(180deg,#0a69b8 0%,#0f7ccd 60%,#1d8fd8 100%)}
.hero-floor{left:0;top:422px;width:1200px;height:72px;background:linear-gradient(#3298dc,var(--blue-light))}
.logo{left:180px;top:92px;display:flex;align-items:center;gap:8px}
.logo-mark{width:22px;height:22px;border-radius:50%;background:var(--cyan)}
.logo-name{font-size:33px;font-weight:700;color:var(--cyan);letter-spacing:-0.5px}
.nav a{position:absolute;top:65px;font-size:12.5px;font-weight:700;color:#fff;text-decoration:none}
.nav .active{left:476px;top:60px;width:63px;height:25px;border-radius:8px;background:linear-gradient(#1f8ad8,#0a4f90);border:2px solid #063d70;text-align:center;padding-top:3px}
.headline{left:182px;top:180px;font-size:30px;font-weight:700;font-style:italic;color:#fff;line-height:31px;letter-spacing:-0.8px}
.subline{left:182px;top:255px;font-size:18px;font-weight:700;font-style:italic;color:#fff;line-height:24px;letter-spacing:-0.5px}
.blurb{left:182px;top:314px;width:400px;font-size:8.8px;line-height:15.5px;color:#fff}
.signup{left:187px;top:398px;width:184px;height:32px;border-radius:16px;background:linear-gradient(#d8f56a,var(--green) 55%,#5c9a08);border:2px solid #a6dc2a;font-size:15px;font-weight:700;color:var(--green-dark);padding:5px 0 0 23px}
.signup svg{position:absolute;right:12px;top:8px}
.monitor{left:606px;top:134px;width:411px;height:258px;border-radius:8px;background:#1c1c1c;border:2px solid #ddd}
.screen{left:620px;top:148px;width:381px;height:229px;border-radius:6px;background:linear-gradient(135deg,#d8c4a0,#e6b9a6 50%,#c99a84)}
.dot{top:470px;width:10px;height:10px;border-radius:50%;background:#777}
.dot.on{background:#1fa9f0}
.crumbs{left:180px;top:513px;width:839px;height:24px;border:1px solid #ddd;border-radius:3px}
.crumb{top:519px;font-size:10px;color:#555}
.crumb b{color:#d33;font-weight:400;font-size:8px;margin-left:3px}
.label{font-size:10px;color:#444}
.field{border:1px solid #ccc;border-radius:3px;background:#fff;font-size:9.5px;color:#999;padding-left:9px;display:flex;align-items:center}
.upload-band{left:180px;top:598px;width:840px;height:45px;background:linear-gradient(#e6e6e6,#fff)}
.chip{height:23px;border-radius:3px;border:1px solid #aaa;background:linear-gradient(#fafafa,#ddd);font-size:10px;color:#444;display:flex;align-items:center;justify-content:center}
.btn-blue{border-radius:3px;background:linear-gradient(#2591dc,#0a62aa);color:#fff;font-size:11px;display:flex;align-items:center;justify-content:center}
.btn-grey{border-radius:3px;background:linear-gradient(#8a8a8a,#5d5d5d);color:#fff;font-size:11.5px;display:flex;align-items:center;justify-content:center}
.section-title{font-size:14px;color:#1a7ac4}
.thead{left:180px;top:684px;width:840px;height:27px;background:linear-gradient(#1d8ad8,#0a64b0);color:#fff;font-size:10.5px}
.thead span{position:absolute;top:7px;transform:translateX(-50%)}
.cell{background:var(--row-bg)}
.cell-text{font-size:11px;color:#666;transform:translateX(-50%)}
.num{width:22px;height:21px;border:1px solid #bbb;background:#fff;font-size:10px;color:#222;text-align:center;padding-top:3px}
.unit{font-size:9.5px;color:#222}
.checkbox{top:971px;width:11px;height:11px;border:1px solid #aaa;background:#fff}
.check-label{top:969px;font-size:9.5px;color:#555}
.footer{left:0;top:1015px;width:1200px;height:75px;background:var(--footer)}
.flink{top:1036px;font-size:9px;color:#fff}
.fsep{top:1035px;font-size:9px;color:#fff}
.social{display:flex;align-items:center;gap:5px;font-size:9.5px;color:#fff}
.social i{width:12px;height:12px;background:#4a9ee0;border-radius:2px;display:block}
</style>
</head>
<body>

<header>
  <div class="abs topbar"></div>
  <span class="abs toplink" style="left:749px">Home</span>
  <span class="abs topsep" style="left:800px">|</span>
  <span class="abs toplink" style="left:826px">Help</span>
  <span class="abs topsep" style="left:871px">|</span>
  <span class="abs toplink" style="left:898px">Sitemap</span>
  <div class="abs login">Login<span class="chev"></span></div>

  <section class="abs hero"></section>
  <div class="abs hero-floor"></div>

  <div class="abs logo"><span class="logo-name">Veldhaven</span><span class="logo-mark"></span></div>

  <nav class="nav">
    <a class="active" style="position:absolute">Home</a>
    <a style="left:578px">About Us</a>
    <a style="left:683px">Team</a>
    <a style="left:768px">Videos</a>
    <a style="left:860px">Clients</a>
    <a style="left:953px">Contact Us</a>
  </nav>

  <h1 class="abs headline">We are a facial recognition<br>analysis company</h1>
  <h2 class="abs subline">We make group of 10 users see a video and analyse<br>their facial expressions</h2>
  <p class="abs blurb">Lorem Ipsum is simply dummy text of the printing and typesetting industry. Lorem Ipsum has been the industry's standard dummy text ever since the 1500s, when an unknown printer took a galley of type and scrambled it to make a type specimen book.</p>

  <div class="abs signup">People to Signup
    <svg width="14" height="16" viewBox="0 0 14 16"><path d="M4 0h6v8h4l-7 8-7-8h4z" fill="#2f5a05"/></svg>
  </div>

  <svg class="abs" style="left:744px;top:390px" width="128" height="76" viewBox="0 0 128 76">
    <defs><linearGradient id="stand" x1="0" x2="1"><stop offset="0" stop-color="#9a9a9a"/><stop offset=".5" stop-color="#f4f4f4"/><stop offset="1" stop-color="#8a8a8a"/></linearGradient></defs>
    <path d="M20 0h88c2 30 6 50 16 62c2 4 0 8-6 8H10c-6 0-8-4-6-8C14 50 18 30 20 0z" fill="url(#stand)"/>
  </svg>
  <div class="abs monitor"></div>
  <div class="abs screen" role="img" aria-label="Close-up portrait with facial analysis guide lines"></div>

  <span class="abs dot on" style="left:961px"></span>
  <span class="abs dot" style="left:975px"></span>
  <span class="abs dot" style="left:990px"></span>
  <span class="abs dot" style="left:1005px"></span>
</header>

<main>
  <div class="abs crumbs"></div>
  <span class="abs crumb" style="left:190px">Home<b>»</b></span>
  <span class="abs crumb" style="left:239px">Project<b>»</b></span>
  <span class="abs crumb" style="left:291px">Media Files<b>»</b></span>
  <span class="abs crumb" style="left:361px">First Commercial<b>»</b></span>

  <span class="abs label" style="left:182px;top:563px">Name :</span>
  <div class="abs field" style="left:218px;top:558px;width:241px;height:23px">First Commercial :</div>

  <div class="abs upload-band"></div>
  <div class="abs chip" style="left:189px;top:609px;width:65px">File Name</div>
  <div class="abs chip" style="left:266px;top:609px;width:64px">Movie 1.avi</div>
  <div class="abs field" style="left:344px;top:610px;width:208px;height:22px">Choose a file
    <svg style="position:absolute;right:8px;top:5px" width="13" height="12" viewBox="0 0 13 12"><circle cx="5" cy="5" r="3.8" fill="none" stroke="#888" stroke-width="1.4"/><path d="M8 7.5l4 3.5" stroke="#888" stroke-width="2"/></svg>
  </div>
  <div class="abs btn-blue" style="left:562px;top:610px;width:54px;height:22px">Upload</div>

  <h3 class="abs section-title" style="left:183px;top:658px;font-weight:400">Stimuli</h3>

  <div class="abs thead">
    <span style="left:86px">Name</span>
    <span style="left:295px">Interval</span>
    <span style="left:503px">Type</span>
  </div>

  <div class="abs cell" style="left:180px;top:715px;width:178px;height:61px"></div>
  <div class="abs cell" style="left:360px;top:715px;width:221px;height:61px"></div>
  <div class="abs cell" style="left:583px;top:715px;width:221px;height:61px"></div>
  <div class="abs cell" style="left:806px;top:715px;width:214px;height:61px"></div>
  <span class="abs cell-text" style="left:271px;top:738px">A</span>
  <span class="abs cell-text" style="left:474px;top:738px">(0:0.00-&gt; 1:10.56)</span>
  <span class="abs cell-text" style="left:691px;top:738px">Positive</span>
  <div class="abs btn-grey" style="left:837px;top:734px;width:54px;height:21px">Edit</div>
  <div class="abs btn-grey" style="left:932px;top:734px;width:70px;height:21px">Remove</div>

  <div class="abs cell" style="left:180px;top:778px;width:178px;height:112px"></div>
  <div class="abs cell" style="left:360px;top:778px;width:221px;height:112px"></div>
  <div class="abs cell" style="left:583px;top:778px;width:221px;height:112px"></div>
  <div class="abs cell" style="left:806px;top:778px;width:214px;height:112px"></div>

  <div class="abs field" style="left:200px;top:826px;width:136px;height:20px">New Stimulis</div>

  <span class="abs label" style="left:387px;top:787px;color:#222">Start Time</span>
  <div class="abs num" style="left:388px;top:811px">1</div><span class="abs unit" style="left:416px;top:820px">m</span>
  <div class="abs num" style="left:440px;top:811px">16</div><span class="abs unit" style="left:468px;top:820px">s</span>
  <div class="abs num" style="left:491px;top:811px">154</div><span class="abs unit" style="left:519px;top:820px">ms</span>
  <span class="abs label" style="left:387px;top:839px;color:#222">End Time</span>
  <div class="abs num" style="left:388px;top:858px">1</div><span class="abs unit" style="left:416px;top:867px">m</span>
  <div class="abs num" style="left:440px;top:858px">16</div><span class="abs unit" style="left:468px;top:867px">s</span>
  <div class="abs num" style="left:491px;top:858px">154</div><span class="abs unit" style="left:519px;top:867px">ms</span>

  <div class="abs field" style="left:629px;top:826px;width:135px;height:20px">Generic
    <svg style="position:absolute;right:2px;top:3px" width="13" height="13" viewBox="0 0 13 13"><rect x=".5" y=".5" width="12" height="12" rx="2" fill="#eee" stroke="#888"/><path d="M3.5 5l3 3 3-3" fill="none" stroke="#333" stroke-width="1.5"/></svg>
  </div>

  <div class="abs btn-grey" style="left:885px;top:824px;width:54px;height:20px">Save</div>
  <div class="abs btn-blue" style="left:968px;top:900px;width:54px;height:21px;font-size:12px">Add</div>

  <h3 class="abs section-title" style="left:182px;top:940px;font-weight:400;font-size:13px">Survey link for this media file :</h3>
  <div class="abs field" style="left:180px;top:966px;width:403px;height:22px;color:#555;font-size:11px;background:linear-gradient(#fff,#f0f0f0)">http://www.samplelink.example/recorder.php?file=Movie1.avi&amp;userid</div>

  <h3 class="abs section-title" style="left:619px;top:940px;font-weight:400;font-size:13px">Link Properties</h3>
  <span class="abs checkbox" style="left:620px"></span><span class="abs check-label" style="left:635px">User Id</span>
  <span class="abs checkbox" style="left:680px"></span><span class="abs check-label" style="left:695px">Independent Variables</span>
  <span class="abs checkbox" style="left:808px"></span><span class="abs check-label" style="left:823px">Use in frame</span>
  <div class="abs btn-blue" style="left:900px;top:961px;width:53px;height:21px;font-size:11.5px">Close</div>
</main>

<footer>
  <div class="abs footer"></div>
  <span class="abs flink" style="left:180px">Home</span><span class="abs fsep" style="left:219px">|</span>
  <span class="abs flink" style="left:236px">About Us</span><span class="abs fsep" style="left:289px">|</span>
  <span class="abs flink" style="left:304px">Team</span><span class="abs fsep" style="left:343px">|</span>
  <span class="abs flink" style="left:358px">Videos</span><span class="abs fsep" style="left:401px">|</span>
  <span class="abs flink" style="left:417px">Clients</span><span class="abs fsep" style="left:460px">|</span>
  <span class="abs flink" style="left:476px">Contact Us</span>
  <span class="abs flink" style="left:180px;top:1058px">Copyright ©2013. <span style="color:#6cc4ff">Veldhaven.</span> All rights reserved.</span>

  <span class="abs flink" style="left:780px;top:1037px;width:100px;text-align:right;line-height:15px">Connect to<br>our Social Network :</span>
  <div class="abs social" style="left:895px;top:1038px"><i></i>Chatterbay</div>
  <div class="abs social" style="left:895px;top:1054px"><i></i>WorkNest</div>
</footer>

</body>
</html>
```